Business Card for Academic Coach

I need a business card designed for me - a private tutor/academic coach.

Glen Mabery
Academic Coach
AB Pellwood University, 1994 Cum Laude
Phone: 404-555-0187
glenrmabery@tutormail-example.com

Subjects
QET and BRT
Math, Physics, Writing

```html
<!DOCTYPE html>
<html lang="en">
<head>
<meta charset="utf-8">
<title>Glen Mabery – Academic Coach Business Card</title>
<link rel="stylesheet" href="https://fonts.googleapis.com/css2?family=Cinzel:wght@400;500&family=Jost:wght@400;500&family=Oswald:wght@600&display=swap">
<style>
  :root {
    --backdrop: #2b2a2a;
    --card: #ffffff;
    --ink-brown: #7b6442;
    --accent-orange: #f5ae3e;
    --ink-dark: #3b3737;
    --emblem-dark: #322e2f;
  }
  * { margin: 0; padding: 0; box-sizing: border-box; }
  html, body {
    width: 1200px;
    height: 1200px;
    overflow: hidden;
  }
  body {
    background: var(--backdrop);
    display: flex;
    align-items: center;
    justify-content: center;
  }
  .business-card {
    width: 560px;
    height: 980px;
    background: var(--card);
    color: var(--ink-brown);
    display: flex;
    flex-direction: column;
    align-items: center;
    text-align: center;
    padding-top: 110px;
  }
  .emblem-placeholder {
    width: 330px;
    height: 110px;
    border-radius: 6px;
    background: linear-gradient(180deg, var(--accent-orange) 0%, #d99a3a 55%, var(--emblem-dark) 100%);
  }
  .coach-name {
    font-family: "Cinzel", serif;
    font-weight: 400;
    font-size: 46px;
    letter-spacing: 1px;
    line-height: 1.2;
    margin-top: 70px;
  }
  .coach-title {
    font-family: "Jost", sans-serif;
    font-weight: 400;
    font-size: 30px;
    line-height: 1.2;
    margin-top: 8px;
  }
  .coach-degree {
    font-family: "Jost", sans-serif;
    font-weight: 400;
    font-size: 21px;
    line-height: 1.3;
    margin-top: 4px;
  }
  .contact-phone {
    font-family: "Cinzel", serif;
    font-size: 34px;
    line-height: 1.2;
    margin-top: 42px;
  }
  .contact-email {
    font-family: "Cinzel", serif;
    font-size: 17.5px;
    letter-spacing: 0.5px;
    line-height: 1.3;
    margin-top: 6px;
  }
  .subjects-badge {
    width: 280px;
    height: 280px;
    border-radius: 50%;
    background: var(--accent-orange);
    border: 2px solid var(--ink-dark);
    color: var(--ink-dark);
    margin-top: 44px;
    display: flex;
    flex-direction: column;
    align-items: center;
    padding-top: 56px;
    font-family: "Jost", sans-serif;
    font-size: 25px;
    line-height: 1.3;
  }
  .subjects-heading {
    font-family: "Oswald", sans-serif;
    font-weight: 600;
    font-size: 36px;
    letter-spacing: 1px;
    line-height: 1.1;
    width: 210px;
    border-bottom: 4px solid var(--ink-dark);
    padding-bottom: 2px;
    margin-bottom: 10px;
  }
</style>
</head>
<body>
  <article class="business-card">
    <div class="emblem-placeholder" role="img" aria-label="Emblem area: open book illustration in orange and dark grey"></div>
    <h1 class="coach-name">GLEN MABERY</h1>
    <p class="coach-title">Academic Coach</p>
    <p class="coach-degree">AB Pellwood University, 1994 Cum Laude</p>
    <p class="contact-phone">404-555-0187</p>
    <p class="contact-email">GLENRMABERY@TUTORMAIL-EXAMPLE.COM</p>
    <section class="subjects-badge">
      <h2 class="subjects-heading">SUBJECTS</h2>
      <p>QET and BRT</p>
      <p>Math, Physics,<br>Writing</p>
    </section>
  </article>
</body>
</html>
```